Etiketten-Design für Weinflasche
Sehr gute Zusammenarbeit bei Tag und Nacht, sehr kooperativ ,flexibel und entgegenkommend. Empfehlenswert
Zielgruppe
Weinbau - Eigenbau Wein -Weinverkauf
Aufgabenstellung
Bräuchte oder Suche ein Flaschenetikette für Rotwein der Marke Zweigelt Das Ausmaß der Etikette sollte 8cm Breit und 12cm Hoch sein. Habe meine letzte Etikette beigelegt sie Anhang

```html
<!DOCTYPE html>
<html lang="de">
<head>
<meta charset="utf-8">
<title>Weinetikett Zweigelt 2020</title>
<link rel="stylesheet" href="https://fonts.googleapis.com/css2?family=Roboto:wght@400&family=Roboto+Condensed:wght@400&display=swap">
<style>
  :root {
    --paper: #ffffff;
    --band: #333333;
    --field: #3e3e3d;
    --field-deep: #363635;
    --muted-text: #5b5c5c;
    --variety-text: #b8b8b8;
    --name-text: #c9c9c9;
    --wine-red: #b01917;
  }
  * { box-sizing: border-box; margin: 0; padding: 0; }
  html, body {
    width: 1200px;
    height: 989px;
    overflow: hidden;
    background: var(--paper);
  }
  .sheet {
    position: relative;
    width: 1200px;
    height: 989px;
  }
  .label {
    position: absolute;
    top: 0;
    width: 573px;
    height: 982px;
    background: var(--band);
    overflow: hidden;
  }
  .label--flat { left: 0; }
  .label--relief { left: 627px; }

  .label__header {
    position: absolute;
    top: 0; left: 0;
    width: 100%;
    height: 164px;
    display: flex;
    align-items: center;
    justify-content: center;
  }
  .label__estate {
    font-family: "Roboto", sans-serif;
    font-weight: 400;
    font-size: 74px;
    letter-spacing: 37px;
    text-indent: 37px;
    color: var(--muted-text);
    line-height: 1;
    margin-top: -4px;
  }
  .label__field {
    position: absolute;
    top: 164px; left: 0;
    width: 100%;
    height: 657px;
  }
  .label__field svg { display: block; width: 100%; height: 100%; }

  .label__mark {
    position: absolute;
    top: 424px;
    left: 0;
    width: 100%;
    height: 52px;
  }
  .label__producer {
    position: absolute;
    right: 314px;
    top: 2px;
    font-family: "Roboto Condensed", sans-serif;
    font-weight: 400;
    font-size: 26px;
    line-height: 23px;
    text-align: right;
    color: var(--name-text);
    text-transform: uppercase;
  }
  .label__dot {
    position: absolute;
    left: 271px;
    top: 8px;
    width: 34px;
    height: 34px;
    background: var(--wine-red);
  }
  .label__variety {
    position: absolute;
    left: 313px;
    top: -7px;
    font-family: "Roboto Condensed", sans-serif;
    font-weight: 400;
    font-size: 60px;
    line-height: 1;
    color: var(--variety-text);
    letter-spacing: 0.5px;
  }

  .label__footer {
    position: absolute;
    top: 821px; left: 0;
    width: 100%;
    height: 161px;
    display: flex;
    align-items: center;
    justify-content: center;
  }
  .label__vintage {
    font-family: "Roboto", sans-serif;
    font-weight: 400;
    font-size: 127px;
    line-height: 1;
    color: var(--muted-text);
    margin-top: -2px;
  }
</style>
</head>
<body>
<main class="sheet">

  <section class="label label--flat">
    <header class="label__header"><span class="label__estate">WEINBAU</span></header>
    <div class="label__field">
      <svg role="img" aria-label="Dunkles Rankenornament mit Weinlaub und Trauben" viewBox="0 0 573 657" preserveAspectRatio="none">
        <defs>
          <radialGradient id="fieldTone1" cx="50%" cy="50%" r="70%">
            <stop offset="0" stop-color="var(--field)"/>
            <stop offset="1" stop-color="var(--field-deep)"/>
          </radialGradient>
        </defs>
        <rect width="573" height="657" fill="url(#fieldTone1)"/>
      </svg>
    </div>
    <div class="label__mark">
      <p class="label__producer">Tobias<br>Lomander</p>
      <span class="label__dot"></span>
      <h1 class="label__variety">ZWEIGELT</h1>
    </div>
    <footer class="label__footer"><span class="label__vintage">2020</span></footer>
  </section>

  <section class="label label--relief">
    <header class="label__header"><span class="label__estate">WEINBAU</span></header>
    <div class="label__field">
      <svg role="img" aria-label="Dunkles Rankenornament mit Weinlaub und Trauben" viewBox="0 0 573 657" preserveAspectRatio="none">
        <defs>
          <radialGradient id="fieldTone2" cx="50%" cy="50%" r="70%">
            <stop offset="0" stop-color="var(--field)"/>
            <stop offset="1" stop-color="var(--field-deep)"/>
          </radialGradient>
        </defs>
        <rect width="573" height="657" fill="url(#fieldTone2)"/>
      </svg>
    </div>
    <div class="label__mark">
      <p class="label__producer">Tobias<br>Lomander</p>
      <span class="label__dot"></span>
      <h2 class="label__variety">ZWEIGELT</h2>
    </div>
    <footer class="label__footer"><span class="label__vintage">2020</span></footer>
  </section>

</main>
</body>
</html>
```